Brambleford Homepage Design

We need a home page design for Brambleford. Brambleford creates gear for outdoor enthusiasts who are passionate about conservation, wildlife observation, and ethical hunting.

Current Website: www.bramblekit.example

Customer Avatar Canvas:
https://sheets.example.net/d/9XqLmRtVwYzAbCdEfGhJkNpQrStUvWxYz12345678/edit#gid=10293847

Homepage Template: Attached below
https://files.example.net/folders/7k3HsPqWmZtRvBnLcXyDfGjQaUeTo

There is info on imagery in the homepage template. Where there isn't, appropriate stock imagery is acceptable.

Logo Design and Product Images: https://files.example.net/folders/4mNbVcXzLkJhGfDsAqWeRtYuIoPzZ

```html
<!DOCTYPE html>
<html lang="en">
<head>
<meta charset="utf-8">
<title>Brambleford — Home</title>
<link rel="stylesheet" href="https://fonts.googleapis.com/css2?family=Poppins:wght@300;400;500;600&display=swap">
<style>
:root{
  --ink:#1f1f1f;
  --muted:#555;
  --dark:#2e2e2e;
  --darker:#262626;
  --light:#f4f4f4;
  --white:#fff;
  --line:#9a9a9a;
  --logo-grey:#8a8a8a;
}
*{box-sizing:border-box;margin:0;padding:0}
html,body{width:1200px;height:5263px;overflow:hidden}
body{font-family:"Poppins",sans-serif;color:var(--ink);background:var(--white);position:relative}
section,header,footer{position:absolute;left:0;width:1200px}
.abs{position:absolute}
.wordmark{font-family:"Poppins",sans-serif;font-weight:600;display:flex;align-items:center;gap:10px}
.wordmark .dot{width:22px;height:22px;border-radius:50%;background:currentColor;flex:none}

/* header */
.site-header{top:0;height:130px;background:var(--white)}
.site-header .wordmark{left:86px;top:46px;font-size:22px;color:var(--ink)}
.nav-link{top:60px;font-size:15px;color:#444}
.shop-btn{left:968px;top:44px;width:146px;height:50px;border-radius:25px;background:#1a1a1a;color:#fff;font-size:12px;font-weight:500;display:flex;align-items:center;justify-content:center}

/* hero */
.hero{top:130px;height:638px;background:linear-gradient(160deg,#5d6a4c 0%,#46583a 40%,#3a5a68 62%,#4d6a35 80%,#3f5529 100%)}
.hero-title{left:88px;font-size:31px;font-weight:400;color:#fff;line-height:41px}
.hero-btn{top:386px;height:84px;border-radius:20px;font-size:14px;line-height:18px;text-align:center;display:flex;align-items:center;justify-content:center}
.hero-btn.primary{left:88px;width:256px;background:#fff;color:var(--ink)}
.hero-btn.ghost{left:360px;width:282px;background:rgba(30,30,30,.75);color:#fff;border:2px solid #fff}
.dots{left:562px;top:568px;display:flex;gap:6px}
.dots span{width:13px;height:13px;border-radius:50%;background:rgba(255,255,255,.5)}
.dots span:first-child{background:#fff}

/* brand strip */
.brand-strip{top:768px;height:288px;background:var(--white)}
.brand-strip .wordmark{top:130px;font-size:21px;color:var(--logo-grey)}

/* video */
.video{top:1056px;height:739px;background:var(--dark)}
.video-frame{left:86px;top:88px;width:1030px;height:422px;background:linear-gradient(120deg,#2b2a24 0%,#4a4131 40%,#6b5a41 55%,#33312a 100%)}
.play{left:458px;top:141px}
.video-cta{left:314px;top:561px;width:572px;height:97px;border-radius:20px;background:#fff;font-size:20px;display:flex;align-items:center;justify-content:center}

/* how it works */
.how{top:1795px;height:1703px;background:var(--white)}
.section-title{width:1200px;text-align:center;font-size:39px;font-weight:500}
.how .sub{top:198px;width:1200px;text-align:center;font-size:19px;color:#444}
.step-photo{width:467px;height:303px}
.step-text{width:468px}
.step-text h3{font-size:17.5px;font-weight:500;line-height:25px;margin-bottom:10px}
.step-text p{font-size:14.5px;line-height:26px;color:var(--muted)}
.timeline{left:603px;top:475px;width:2px;height:1030px;background:var(--line)}
.step-num{left:583px;width:42px;height:42px;border-radius:50%;border:1.5px solid #777;background:#fff;font-size:17px;color:#555;display:flex;align-items:center;justify-content:center}

/* audience */
.audience{top:3498px;height:929px;background:var(--dark);color:#fff}
.audience .section-title{top:126px;color:#fff}
.aud-badge{width:100px;height:80px;background:#fff;border-radius:4px;color:var(--ink);font-size:12px;justify-content:center}
.aud-badge .dot{width:10px;height:10px}
.aud-text{width:485px;font-size:14.5px;line-height:26px;text-align:justify;color:#e8e8e8}

/* cta */
.cta{top:4427px;height:446px;background:var(--light)}
.cta .section-title{top:110px;font-size:38px;line-height:48px}
.cta-btn{left:290px;top:239px;width:630px;height:96px;border-radius:10px;background:#2b2b2b;color:#fff;font-size:23px;display:flex;align-items:center;justify-content:center}

/* footer */
.site-footer{top:4873px;height:390px;background:var(--darker);color:#fff}
.site-footer .wordmark{left:86px;top:110px;font-size:28px;color:#fff}
.foot-head{top:78px;font-size:19px;font-weight:500}
.foot-list{list-style:none;font-size:15px}
.foot-list li{height:42px;display:flex;align-items:center;gap:14px}
.bullet{width:6px;height:6px;border-radius:50%;background:#fff}
.contact-row{display:flex;align-items:center;gap:10px;font-size:16px}
.ico{width:22px;height:22px;border-radius:50%;background:#fff;display:flex;align-items:center;justify-content:center;flex:none}
.social{display:flex;align-items:center;gap:14px;font-size:10px}
.social .ico{width:28px;height:28px;background:#4a4a4a}
.social .ico span{width:8px;height:8px;border-radius:50%;background:#fff}
.bottom-bar{left:0;top:347px;width:1200px;height:43px;border-top:1px solid #3a3a3a;font-size:13px;color:#ddd}
</style>
</head>
<body>

<header class="site-header">
  <div class="abs wordmark"><span class="dot"></span>Brambleford</div>
  <nav>
    <span class="abs nav-link" style="left:690px">Features</span>
    <span class="abs nav-link" style="left:793px">About Us</span>
    <span class="abs nav-link" style="left:899px">Log In</span>
  </nav>
  <a class="abs shop-btn">SHOP GEAR</a>
</header>

<section class="hero" role="img" aria-label="Hunter with binoculars on a mountain slope above an alpine lake">
  <h1 class="abs hero-title" style="top:113px">“Explore the Wild West: Embrace Conservation,<br>Hunt Ethically, and Protect Public Lands with Brambleford Gear"</h1>
  <p class="abs hero-title" style="top:228px">"Elevate Your Outdoor Adventures<br>While Supporting Conservation Efforts"</p>
  <a class="abs hero-btn primary">Order Your Brambleford<br>Bino Harness Today!</a>
  <a class="abs hero-btn ghost">Unlock the Power of Optics<br>and Preserve the Wild</a>
  <div class="abs dots"><span></span><span></span><span></span><span></span></div>
</section>

<section class="brand-strip">
  <div class="abs wordmark" style="left:130px"><span class="dot"></span>Brambleford</div>
  <div class="abs wordmark" style="left:326px"><span class="dot"></span>Brambleford</div>
  <div class="abs wordmark" style="left:530px"><span class="dot"></span>Brambleford</div>
  <div class="abs wordmark" style="left:724px"><span class="dot"></span>Brambleford</div>
  <div class="abs wordmark" style="left:915px"><span class="dot"></span>Brambleford</div>
</section>

<section class="video">
  <div class="abs video-frame" role="img" aria-label="Video still of a bull elk standing among forest trees">
    <svg class="abs play" width="114" height="114" viewBox="0 0 114 114"><circle cx="57" cy="57" r="55" fill="#fff"/><path d="M44 34 L82 57 L44 80 Z" fill="#222"/></svg>
  </div>
  <a class="abs video-cta">Order Your Brambleford Bino Harness Today!</a>
</section>

<section class="how">
  <h2 class="abs section-title" style="top:112px">How It Works</h2>
  <p class="abs sub">Introducing the Brambleford Bino Harness – The Ultimate Companion for Your Optics</p>
  <div class="abs timeline"></div>

  <div class="abs step-photo" style="left:82px;top:285px;background:linear-gradient(135deg,#7a6a3a,#b89a55 50%,#5c5a3a)" role="img" aria-label="Hunter kneeling beside large elk antlers on a grassy hillside"></div>
  <div class="abs step-num" style="top:462px">1</div>
  <div class="abs step-text" style="left:647px;top:340px">
    <h3>STEP 1: Experience unparalleled convenience and comfort during your outdoor excursions with the Brambleford Bino Harness</h3>
    <p>Designed specifically for the modern conservationist and avid hunter, this innovative harness combines functionality, durability, and style to enhance your ildlife observation and hunting experiences.</p>
  </div>

  <div class="abs step-text" style="left:86px;top:690px">
    <h3>STEP 2: Unmatched Optics Protection:</h3>
    <p>Our Bino Harness features a secure and adjustable harness system that keeps your binoculars safe and within easy reach at all times. No more fumbling around or worry-ing about accidentally dropping your expensive optics. With the Brambleford Bino Harness, your binoculars are securely trapped to your chest, ffering quick and hassle-free access whenever you need them.</p>
  </div>
  <div class="abs step-num" style="top:755px">2</div>
  <div class="abs step-photo" style="left:647px;top:635px;background:linear-gradient(160deg,#5d86c4,#c9d6e6 45%,#6b5a48 75%,#8c7a60)" role="img" aria-label="Hunter with a bighorn sheep on a snowy mountain ridge under blue sky"></div>

  <div class="abs step-photo" style="left:82px;top:996px;background:linear-gradient(135deg,#4d5a2a,#a08a3a 50%,#6a6a2c)" role="img" aria-label="Smiling hunter seated in golden grass holding deer antlers"></div>
  <div class="abs step-num" style="top:1121px">3</div>
  <div class="abs step-text" style="left:647px;top:1052px">
    <h3>STEP 3: Thoughtful Design for Easy Access:</h3>
    <p>We've incorporated thoughtful design elements into the Brambleford Bino Harness to enhance your outdoor adventures. The quick-release buckles allow for swift and effortless removal of the harness, granting you unhindered mobility when necessary. The adjustable straps ensure a personalized fit for individuals of all body types,</p>
  </div>

  <div class="abs step-text" style="left:86px;top:1405px">
    <h3>STEP 4: Embrace Conservation:</h3>
    <p>By choosing the Brambleford Bino Harness, you're not only in-vesting in a premium gear accessory but also supporting the conservation of public lands and wildlife. We are dedicated to promoting sustainable hunting and ethical practices, and a portion of the proceeds from every purchase goes towards initiatives that preserve the habitats we hold dear.</p>
  </div>
  <div class="abs step-num" style="top:1474px">4</div>
  <div class="abs step-photo" style="left:647px;top:1347px;background:linear-gradient(170deg,#d6c8b0,#b09a78 45%,#6a5a40 80%)" role="img" aria-label="Hunter glassing with binoculars among dry brush in open hills"></div>
</section>

<section class="audience">
  <h2 class="abs section-title">Who It’s For</h2>
  <div class="abs wordmark aud-badge" style="left:86px;top:246px"><span class="dot"></span>Brambleford</div>
  <p class="abs aud-text" style="left:86px;top:362px">The Brambleford Bino Harness is the ideal gear accessory for outdoor enthusiasts who are passionate about conservation, wildlife observation, and ethical hunting. This product is designed for individuals who value the preservation of public lands, appreciate the beauty of the American West, and seek to engage in sustainable and responsible outdoor pursuits.</p>
  <div class="abs wordmark aud-badge" style="left:630px;top:246px"><span class="dot"></span>Brambleford</div>
  <p class="abs aud-text" style="left:630px;top:362px">This harness is perfect for avid hunters who want quick and easy access to their binoculars without compromising on comfort. It is also ideal for wildlife photographers, birdwatchers, and nature enthusiasts who rely on high-quality optics to capture stunning images or observe wildlife in their natural habitats.</p>
  <div class="abs wordmark aud-badge" style="left:86px;top:567px"><span class="dot"></span>Brambleford</div>
  <p class="abs aud-text" style="left:86px;top:684px">Additionally, the Brambleford Bino Harness appeals to those who prioritize durability and reliability in their gear. Whether you're exploring rugged terrains, participating in long hikes, or embarking on extended hunting trips, this harness will securely hold your binoculars, providing peace of mind and allowing you to focus on the beauty of nature.</p>
  <div class="abs wordmark aud-badge" style="left:630px;top:567px"><span class="dot"></span>Brambleford</div>
  <p class="abs aud-text" style="left:630px;top:684px;text-align:left">The Brambleford Bino Harness is designed for outdoor enthusiasts who embrace a conservation-centered lifestyle, value ethical hunting practices, and appreciate the unique opportunities offered by the American West.</p>
</section>

<section class="cta">
  <h2 class="abs section-title">Unlock the Power of Optics and<br>Preserve the Wild</h2>
  <a class="abs cta-btn">Order Your Brambleford Bino Harness Today!</a>
</section>

<footer class="site-footer">
  <div class="abs wordmark"><span class="dot"></span>Brambleford</div>

  <h4 class="abs foot-head" style="left:366px">QUIK LINKS</h4>
  <ul class="abs foot-list" style="left:366px;top:117px">
    <li><span class="bullet"></span>Feautures</li>
    <li><span class="bullet"></span>About Us</li>
    <li><span class="bullet"></span>Log In</li>
  </ul>

  <h4 class="abs foot-head" style="left:606px">CONTACT US</h4>
  <div class="abs contact-row" style="left:610px;top:131px">
    <span class="ico"><svg width="12" height="12" viewBox="0 0 24 24"><path d="M6.6 10.8a15 15 0 0 0 6.6 6.6l2.2-2.2c.3-.3.7-.4 1-.2 1.1.4 2.3.6 3.6.6.6 0 1 .4 1 1V20c0 .6-.4 1-1 1A17 17 0 0 1 3 4c0-.6.4-1 1-1h3.5c.6 0 1 .4 1 1 0 1.3.2 2.5.6 3.6.1.3 0 .7-.2 1z" fill="#262626"/></svg></span>+012 345 6789
  </div>
  <div class="abs contact-row" style="left:610px;top:183px;font-size:15px">
    <span class="ico"><svg width="12" height="10" viewBox="0 0 24 18"><rect x="1" y="1" width="22" height="16" rx="2" fill="none" stroke="#262626" stroke-width="2.5"/><path d="M2 3l10 7 10-7" fill="none" stroke="#262626" stroke-width="2.5"/></svg></span>info@brambleford.example
  </div>
  <div class="abs contact-row" style="left:610px;top:240px;font-size:14px;line-height:17px">
    <span class="ico"><svg width="10" height="13" viewBox="0 0 20 26"><path d="M10 0a9 9 0 0 0-9 9c0 7 9 17 9 17s9-10 9-17a9 9 0 0 0-9-9zm0 12a3 3 0 1 1 0-6 3 3 0 0 1 0 6z" fill="#262626"/></svg></span>Address line Dummy Here<br>Address line Here
  </div>

  <h4 class="abs foot-head" style="left:875px">FOLLOW US</h4>
  <div class="abs social" style="left:875px;top:129px"><span class="ico"><span></span></span>Friendbook</div>
  <div class="abs social" style="left:1020px;top:129px"><span class="ico"><span></span></span>ViewTube</div>
  <div class="abs social" style="left:875px;top:171px"><span class="ico"><span></span></span>Snapgram</div>
  <div class="abs social" style="left:1020px;top:171px"><span class="ico"><span></span></span>LinkNet</div>
  <div class="abs social" style="left:875px;top:213px"><span class="ico"><span></span></span>Chirper</div>

  <div class="abs bottom-bar">
    <span class="abs" style="left:86px;top:12px">Copyright © 2023 All Rights Reserved By Brambleford</span>
    <span class="abs" style="left:898px;top:12px">Terms of Service | Privacy Policy</span>
  </div>
</footer>

</body>
</html>
```